4 Ridges Commercial Group Commercial Real Estate Sign

Real estate sign design for 4X4 and 4X8 sizes. I included the back of our business cards, the 4 Ridges Commercial Group Logo, the 4R Logo and the Brokered by vOm logo. Regardless of design, it needs to have the 'Brokered by' vOm logo somewhere on the sign, preferably on the bottom corner or somewhere smaller then the rest. Looking for a unique, professional, modern look.

Target Market(s)

Commercial Realtors and clients

Requirements
Must have
• Must include in smaller letters "Brokered by vOm Realty" or the logo attached. Need two designs one that says For Sale, and one that says For Lease.
• Please see attached sign example. We need a sign like this, but want a creative cool design that is unique and professional.

```html
<!DOCTYPE html>
<html lang="en">
<head>
<meta charset="utf-8">
<title>4 Ridges Commercial Group – For Lease Sign</title>
<link href="https://fonts.googleapis.com/css2?family=Cinzel:wght@400;600;700&display=swap" rel="stylesheet">
<style>
  :root {
    --navy: #13275f;
    --navy-text: #1b2f6e;
    --gold: #f7b117;
    --white: #ffffff;
    --backdrop: #a9a9a9;
  }
  * { margin: 0; padding: 0; box-sizing: border-box; }
  html, body { width: 1200px; height: 1000px; overflow: hidden; }
  body {
    background: var(--backdrop);
    font-family: "Cinzel", "Times New Roman", serif;
  }
  .sign {
    position: absolute;
    left: 170px; top: 45px;
    width: 860px; height: 890px;
    background: var(--white);
    overflow: hidden;
  }
  .sign-bands { position: absolute; inset: 0; }
  .brand {
    position: absolute;
    left: 0; right: 0; top: 80px;
    display: flex; align-items: center; justify-content: center; gap: 28px;
    color: var(--navy-text);
    font-weight: 600;
  }
  .brand-mark {
    width: 96px; height: 96px;
    border-radius: 50%;
    background: var(--navy-text);
  }
  .brand-name { line-height: 1; }
  .brand-name .primary { display: block; font-size: 66px; letter-spacing: 1px; }
  .brand-name .secondary { display: block; font-size: 22px; letter-spacing: 7px; margin-top: 10px; }
  .headline {
    position: absolute; left: 0; right: 0; top: 378px;
    text-align: center;
    color: var(--white);
    font-size: 104px; font-weight: 400;
    letter-spacing: 2px; line-height: 1;
  }
  .agents {
    position: absolute; left: 0; right: 0; top: 550px;
    display: flex; justify-content: center;
  }
  .agent { width: 420px; text-align: center; }
  .agent-name { color: var(--white); font-size: 42px; font-weight: 400; line-height: 1; }
  .agent-phone { color: var(--gold); font-size: 56px; font-weight: 600; line-height: 1; margin-top: 14px; }
  .agent-divider { width: 3px; height: 104px; background: var(--gold); margin-top: 2px; }
  .website {
    position: absolute; left: 0; right: 0; top: 700px;
    text-align: center;
    color: var(--white);
    font-size: 50px; font-weight: 700; line-height: 1;
  }
  .website .accent { color: var(--gold); }
  .broker {
    position: absolute; left: 0; right: 0; top: 790px;
    text-align: center;
    color: var(--white);
    font-size: 17px; font-weight: 600; letter-spacing: 1px;
  }
</style>
</head>
<body>
  <div class="sign">
    <svg class="sign-bands" width="860" height="890" viewBox="0 0 860 890" aria-hidden="true">
      <path d="M0,253 Q430,385 860,263 L860,890 L0,890 Z" fill="var(--gold)"/>
      <path d="M0,260 Q430,412 860,295 L860,870 L0,870 Z" fill="var(--navy)"/>
    </svg>

    <div class="brand">
      <div class="brand-mark"></div>
      <div class="brand-name">
        <span class="primary">4 Ridges</span>
        <span class="secondary">Commercial Group</span>
      </div>
    </div>

    <div class="headline">FOR LEASE</div>

    <div class="agents">
      <div class="agent">
        <div class="agent-name">Marcus Delgado</div>
        <div class="agent-phone">512.555.0142</div>
      </div>
      <div class="agent-divider"></div>
      <div class="agent">
        <div class="agent-name">Thomas Whitfield</div>
        <div class="agent-phone">214.555.0187</div>
      </div>
    </div>

    <div class="website">www.<span class="accent">4R</span>.Life</div>

    <div class="broker">Brokered by vOm Realty</div>
  </div>
</body>
</html>
```